Plakat-Design für Verkaufs-o. Fensternasen
Briefing und Kommunikation waren sehr angenehm und unkompliziert, immer wieder gerne.
Zielgruppe
Immobilien & Hausverwaltungen

```html
<!DOCTYPE html>
<html lang="de">
<head>
<meta charset="utf-8">
<title>Fensternasen-Plakate – Heinrich Albers Immobilien</title>
<link rel="stylesheet" href="https://fonts.googleapis.com/css2?family=Source+Sans+3:wght@400;600;700&display=swap">
<style>
  :root {
    --sign-red: #e20d1d;
    --sign-navy: #2b2f80;
    --brand-blue: #4a4ea6;
    --paper: #ffffff;
    --backdrop: #ffffff;
    --edge: #c9c9c9;
  }
  * { box-sizing: border-box; margin: 0; padding: 0; }
  html, body {
    width: 1200px; height: 1200px; overflow: hidden;
    background: var(--backdrop);
    font-family: "Source Sans 3", "Segoe UI", Arial, sans-serif;
  }
  .board { position: relative; width: 1200px; height: 1200px; }
  .sign {
    position: absolute; top: 256px;
    width: 454px; height: 690px;
    background: var(--paper);
    border: 1px solid var(--edge);
    box-shadow: 0 2px 6px rgba(0,0,0,0.15);
    text-align: center;
  }
  .sign--buy { left: 114px; }
  .sign--rent { left: 632px; }

  .sign__headline {
    position: absolute; top: 0; left: 0; right: 0; height: 146px;
    background: var(--sign-red); color: var(--paper);
    font-weight: 700; font-size: 72px; letter-spacing: 1px;
    line-height: 146px;
  }
  .brand__mark {
    position: absolute; top: 232px; left: 212px;
  }
  .brand__name {
    position: absolute; top: 280px; left: 0; right: 0;
    font-weight: 600; font-size: 56px; line-height: 56px;
    color: var(--brand-blue);
  }
  .brand__claim {
    position: absolute; top: 334px; left: 0; right: 26px;
    text-align: right;
    font-size: 26px; line-height: 28px; color: var(--sign-red);
  }
  .brand__since {
    position: absolute; top: 364px; left: 0; right: 26px;
    text-align: right;
    font-size: 15px; line-height: 18px; color: var(--sign-red);
  }
  .office {
    position: absolute; top: 397px; left: 0; right: 0;
    font-weight: 600; font-size: 28px; line-height: 35px;
    color: var(--sign-navy);
  }
  .web {
    position: absolute; top: 512px; left: 0; right: 0;
    font-weight: 600; font-size: 44px; line-height: 56px;
    color: var(--sign-red);
  }
  .phone {
    position: absolute; left: 0; right: 0; bottom: 0; height: 108px;
    background: var(--sign-navy); color: var(--paper);
    display: flex; align-items: center; justify-content: center; gap: 14px;
    font-weight: 600; font-size: 46px;
  }
  .phone__icon { width: 48px; height: 48px; }
</style>
</head>
<body>
<main class="board">

  <section class="sign sign--buy">
    <h1 class="sign__headline">ZU KAUFEN</h1>
    <svg class="brand__mark" width="28" height="28" viewBox="0 0 28 28" aria-hidden="true"><rect width="28" height="28" fill="var(--brand-blue)"/></svg>
    <div class="brand__name">Heinrich Albers</div>
    <div class="brand__claim">Ihr Zuhause im Blick.</div>
    <div class="brand__since">Seit 1982 vor Ort.</div>
    <p class="office">Immobilien VIM<br>Lindenplatz 14 – Kempen</p>
    <p class="web">heinrich-albers.de</p>
    <div class="phone">
      <svg class="phone__icon" viewBox="0 0 48 48" aria-hidden="true">
        <circle cx="24" cy="24" r="23" fill="var(--paper)"/>
        <path d="M17 11c1.5-.6 2.6.2 3.3 1.5l2.4 4.6c.6 1.2.3 2.4-.8 3.2l-2 1.4c1 3 3.5 6.3 6.3 8.2l1.8-1.6c1-.9 2.3-1 3.4-.3l4.3 2.7c1.2.8 1.7 2 1 3.4-1.4 2.8-4 4.3-7 3.4C21.8 35.5 13.6 27 12.2 18.5c-.4-3.2 1.9-6.3 4.8-7.5z" fill="var(--sign-navy)"/>
      </svg>
      <span>02161 - 48 27 0</span>
    </div>
  </section>

  <section class="sign sign--rent">
    <h1 class="sign__headline">ZU MIETEN</h1>
    <svg class="brand__mark" width="28" height="28" viewBox="0 0 28 28" aria-hidden="true"><rect width="28" height="28" fill="var(--brand-blue)"/></svg>
    <div class="brand__name">Heinrich Albers</div>
    <div class="brand__claim">Ihr Zuhause im Blick.</div>
    <div class="brand__since">Seit 1982 vor Ort.</div>
    <p class="office">Immobilien VIM<br>Lindenplatz 14 – Kempen</p>
    <p class="web">heinrich-albers.de</p>
    <div class="phone">
      <svg class="phone__icon" viewBox="0 0 48 48" aria-hidden="true">
        <circle cx="24" cy="24" r="23" fill="var(--paper)"/>
        <path d="M17 11c1.5-.6 2.6.2 3.3 1.5l2.4 4.6c.6 1.2.3 2.4-.8 3.2l-2 1.4c1 3 3.5 6.3 6.3 8.2l1.8-1.6c1-.9 2.3-1 3.4-.3l4.3 2.7c1.2.8 1.7 2 1 3.4-1.4 2.8-4 4.3-7 3.4C21.8 35.5 13.6 27 12.2 18.5c-.4-3.2 1.9-6.3 4.8-7.5z" fill="var(--sign-navy)"/>
      </svg>
      <span>02161 - 48 27 0</span>
    </div>
  </section>

</main>
</body>
</html>
```